D*mn Those Cozy Walls - Dare Boldly, Claim Center Stage Within Every Day: UPCOMING BOOK

We want a Book Cover for a book that will be published shortly. Some options we originally created are attached but they are not really working but give an idea of the text that needs to be on there. We want it to look like a quality book. Tessa is a well known acting coach, and we have some amazing celebrity quotes for the front cover - but it doesn't HAVE to reflect the acting world, the book is for everyone. We want something that represents freedom a sense of release, INSPIRATIONAL - but not cheesy. No flowers or images like that. Simple and authentic is best... Happy to try some with text only and just block colors - the title needs to POP. It's long but we want the Dare Boldly part to pop as well.

```html
<!DOCTYPE html>
<html lang="en">
<head>
<meta charset="utf-8">
<title>D*mn Those Cozy Walls — Book Cover</title>
<link rel="stylesheet" href="https://fonts.googleapis.com/css2?family=Montserrat:wght@500;600;700;800;900&family=Great+Vibes&display=swap">
<style>
  :root {
    --night: #0f1838;
    --navy: #1b2450;
    --deep-blue: #2b3f86;
    --mid-blue: #4a6fb8;
    --mist: #9fb8e0;
    --haze: #c8d6ee;
    --rock: #1a1f2e;
    --white: #ffffff;
    --band: rgba(255, 255, 255, 0.92);
    --ink: #1c2350;
  }
  * { margin: 0; padding: 0; box-sizing: border-box; }
  html, body {
    width: 896px;
    height: 1200px;
    overflow: hidden;
    background: var(--night);
  }
  .cover {
    position: relative;
    width: 896px;
    height: 1200px;
    overflow: hidden;
    font-family: "Montserrat", sans-serif;
    color: var(--white);
    text-align: center;
  }
  .cover-scene {
    position: absolute;
    inset: 0;
    background:
      radial-gradient(ellipse 60% 30% at 75% 18%, rgba(140, 90, 170, 0.35), transparent 70%),
      linear-gradient(180deg,
        var(--night) 0%,
        var(--navy) 18%,
        var(--deep-blue) 38%,
        var(--mid-blue) 55%,
        var(--mist) 68%,
        var(--haze) 74%,
        var(--mid-blue) 84%,
        var(--rock) 100%);
  }
  .author-band {
    position: absolute;
    top: 0; left: 0; right: 0;
    height: 200px;
    background: linear-gradient(180deg, rgba(12, 18, 45, 0.85), rgba(12, 18, 45, 0.35));
  }
  .author-name {
    position: absolute;
    top: 82px; left: 0; right: 0;
    font-weight: 700;
    font-size: 46px;
    letter-spacing: 6px;
  }
  .author-role {
    position: absolute;
    top: 148px; left: 0; right: 0;
    font-weight: 500;
    font-size: 26px;
    letter-spacing: 0.5px;
  }
  .title-lead {
    position: absolute;
    top: 232px; left: 0; right: 0;
    font-weight: 800;
    font-size: 96px;
    letter-spacing: 1px;
    line-height: 1;
  }
  .title-band {
    position: absolute;
    top: 362px; left: 0; right: 0;
    height: 104px;
    background: var(--band);
    display: flex;
    align-items: center;
    justify-content: center;
  }
  .title-main {
    font-weight: 900;
    font-size: 96px;
    color: var(--ink);
    letter-spacing: 2px;
    line-height: 1;
  }
  .tagline {
    position: absolute;
    left: 0; right: 0;
    font-family: "Great Vibes", cursive;
    color: var(--white);
    line-height: 1.1;
  }
  .tagline-dare {
    top: 482px;
    font-size: 70px;
  }
  .tagline-claim {
    top: 852px;
    font-size: 54px;
  }
  .endorsement {
    position: absolute;
    top: 1012px; left: 0; right: 0;
  }
  .endorsement-quote {
    font-weight: 500;
    font-size: 30px;
  }
  .endorsement-name {
    margin-top: 8px;
    font-weight: 700;
    font-size: 30px;
    letter-spacing: 1px;
  }
</style>
</head>
<body>
  <main class="cover">
    <div class="cover-scene" role="img" aria-label="Photograph of a starry night sky over misty blue mountain ridges, with a person leaping between two dark rock ledges in the foreground"></div>

    <header class="author-band">
      <p class="author-name">TESSA MARLOW</p>
      <p class="author-role">Hollywood #1 Acting Coach</p>
    </header>

    <h1 class="title">
      <span class="title-lead">D*mn Those</span>
      <span class="title-band"><span class="title-main">COZY WALLS</span></span>
    </h1>

    <p class="tagline tagline-dare">Dare Boldly</p>
    <p class="tagline tagline-claim">Claim Center Stage<br>Within Every Day</p>

    <footer class="endorsement">
      <p class="endorsement-quote">"I d*mn love this book ...."</p>
      <p class="endorsement-name">DANA RUELL</p>
    </footer>
  </main>
</body>
</html>
```